Business Card Design for Animal Clinic

We are seeking a two sided business card design. The primary side should include our logo (provided in AI and EPS files) address, phone, website, and if possible "Follow Us" with icons for Facebook, Google+, and Twitter.

The back of the card needs to included space for appointment reminders.

Company Name:
Calderbrook Animal Clinic

Doctor Name:
To be provided to winner

Adress:
To be provided to winner

Phone:
to be provided to winner

Website:
www.calderbrookanimalclinic.com

```html
<!DOCTYPE html>
<html lang="en">
<head>
<meta charset="utf-8">
<title>Calderbrook Animal Clinic – Business Card</title>
<link href="https://fonts.googleapis.com/css2?family=Open+Sans:wght@400;500&display=swap" rel="stylesheet">
<style>
  :root {
    --stage: #000000;
    --brick: #a8352e;
    --peach: #d4977a;
    --paper: #ffffff;
    --white: #ffffff;
  }
  html, body {
    margin: 0;
    padding: 0;
    width: 1000px;
    height: 1200px;
    overflow: hidden;
    background: var(--stage);
    font-family: "Open Sans", Arial, sans-serif;
  }
  .canvas {
    position: relative;
    width: 1000px;
    height: 1200px;
  }

  /* Front side */
  .card-front {
    position: absolute;
    left: 80px;
    top: 69px;
    width: 849px;
    height: 495px;
    background: var(--brick);
  }
  .front-pattern {
    position: absolute;
    inset: 0;
    background: radial-gradient(ellipse at 50% 45%, #b03a32 0%, var(--brick) 70%);
  }
  .brand-name {
    position: absolute;
    left: 0;
    right: 0;
    text-align: center;
    font-weight: 400;
    text-transform: uppercase;
    margin: 0;
  }
  .card-front .brand-name {
    top: 225px;
    color: var(--white);
    font-size: 60px;
    letter-spacing: 4px;
    line-height: 1.15;
  }
  .card-front .brand-name span {
    display: block;
    font-size: 30px;
    letter-spacing: 6px;
  }

  /* Back side */
  .card-back {
    position: absolute;
    left: 73px;
    top: 643px;
    width: 860px;
    height: 502px;
    background: var(--paper);
  }
  .band { position: absolute; left: 0; width: 100%; }
  .band--brick-top { top: 0; height: 23px; background: var(--brick); }
  .band--peach-top { top: 34px; height: 7px; background: var(--peach); }
  .band--peach-bottom { top: 463px; height: 7px; background: var(--peach); }
  .band--brick-bottom { top: 479px; height: 23px; background: var(--brick); }

  .card-back .brand-name {
    left: 40px;
    right: auto;
    width: 380px;
    top: 182px;
    color: var(--brick);
    font-size: 36px;
    letter-spacing: 2px;
    line-height: 1.2;
  }
  .card-back .brand-name span {
    display: block;
    font-size: 20px;
    letter-spacing: 4px;
  }

  .divider {
    position: absolute;
    left: 430px;
    top: 77px;
    width: 2px;
    height: 330px;
    background: var(--brick);
  }
  .doctor-name {
    position: absolute;
    left: 529px;
    top: 145px;
    margin: 0;
    color: var(--brick);
    font-size: 23px;
    font-weight: 500;
  }
  .contact-list {
    position: absolute;
    left: 447px;
    top: 257px;
    margin: 0;
    padding: 0;
    list-style: none;
  }
  .contact-item {
    display: flex;
    align-items: center;
    height: 44px;
    margin-bottom: 9px;
    color: var(--brick);
    font-size: 18px;
    font-weight: 500;
  }
  .contact-icon {
    width: 44px;
    height: 44px;
    background: var(--peach);
    margin-right: 14px;
    flex: none;
  }
</style>
</head>
<body>
<main class="canvas">

  <section class="card-front" aria-label="Card front">
    <div class="front-pattern" role="img" aria-label="Scattered soft heart pattern background"></div>
    <p class="brand-name">Calderbrook<span>Animal Clinic</span></p>
  </section>

  <section class="card-back" aria-label="Card back">
    <div class="band band--brick-top"></div>
    <div class="band band--peach-top"></div>

    <p class="brand-name">Calderbrook<span>Animal Clinic</span></p>

    <div class="divider"></div>

    <h2 class="doctor-name">Doctor Name</h2>

    <ul class="contact-list">
      <li class="contact-item">
        <svg class="contact-icon" viewBox="0 0 44 44" aria-hidden="true">
          <path d="M10 22 L22 11 L34 22" fill="none" stroke="#fff" stroke-width="3"/>
          <path d="M14 21 V33 H30 V21" fill="none" stroke="#fff" stroke-width="3"/>
          <rect x="19" y="25" width="6" height="8" fill="#fff"/>
        </svg>
        ashgrove lane, hy- 4821
      </li>
      <li class="contact-item">
        <svg class="contact-icon" viewBox="0 0 44 44" aria-hidden="true">
          <path d="M14 10 L19 10 L21 17 L18 19 C19.5 23 21.5 25 25 26.5 L27 23.5 L34 25.5 V30 C34 32 32 34 30 34 C20 33 11 24 10 14 C10 12 12 10 14 10 Z" fill="#fff"/>
        </svg>
        555-20718
      </li>
      <li class="contact-item">
        <svg class="contact-icon" viewBox="0 0 44 44" aria-hidden="true">
          <g fill="none" stroke="#fff" stroke-width="2">
            <circle cx="22" cy="22" r="12"/>
            <ellipse cx="22" cy="22" rx="5" ry="12"/>
            <line x1="10" y1="22" x2="34" y2="22"/>
            <path d="M12 16 H32 M12 28 H32"/>
          </g>
        </svg>
        www.calderbrookanimalclinic.com
      </li>
    </ul>

    <div class="band band--peach-bottom"></div>
    <div class="band band--brick-bottom"></div>
  </section>

</main>
</body>
</html>
```